Holiday Sale 2026 Graphics for New Year

I want to create 10 social media graphics (new Instagram size 4:5 (1080 x 1350 pixels) focusing on our Holiday Sale Graphics, using any of the pics attached. Use the attached pics, NO RANDOM STOCK PHOTOGRAPHY. For the color scheme of the graphics, they should all be complementary to the product colors in the photos.
You can add any of the photos attached but none are required. You can do some of the graphics in all text. I mainly need BOLD text that says one of the headlines with the pics (10 total):
1. 25% OFF Holiday Sale: New You Starts Now!
2. 25% OFF Everything: New Year, New You
3. 25% OFF Christmas Sale 🎁 Feel Amazing Again!
4. Holiday Treat: 25% OFF Your Favorites
5. 25% OFF All Supplements ✨ New Year Reset!
6. Holiday Magic: 25% OFF Every Supplement
7. 25% OFF to Kickstart Your New Year Goals
8. New Year, New Waistline! 25% OFF Sale
9. Holiday Sale: 25% OFF Everything
10. A Better You Begins With 25% OFF

```html
<!DOCTYPE html>
<html lang="en">
<head>
<meta charset="utf-8">
<title>Holiday Sale Social Graphics</title>
<link rel="stylesheet" href="https://fonts.googleapis.com/css2?family=Bebas+Neue&display=swap">
<style>
  :root {
    --canvas: #d2d3d5;
    --blue-ink: #1f4fa8;
    --blue-soft: #b3c7ea;
    --blue-deep: #3b49a1;
    --blue-pale: #c8dcf5;
    --green-deep: #2e5a55;
    --green-mid: #8fbfa6;
    --green-pale: #c9e4d5;
    --mint-bg: #c2e1d1;
    --mint-circle: #95c2a9;
    --plum: #8c2b88;
    --plum-deep: #92308a;
    --orchid: #b466ad;
    --orchid-light: #d08bc5;
    --pink-pale: #f6c4e2;
    --pink-mid: #d98fcb;
  }
  * { margin: 0; padding: 0; box-sizing: border-box; }
  html, body { width: 1200px; height: 612px; overflow: hidden; background: var(--canvas); }
  .board { position: relative; width: 1200px; height: 612px; }
  .post { position: absolute; width: 217.6px; height: 272px; display: block; }
  .post text { font-family: "Bebas Neue", "Oswald", sans-serif; text-anchor: start; }
  .ink-blue { fill: var(--blue-ink); }
  .ink-blue-pale { fill: var(--blue-pale); }
  .ink-green-deep { fill: var(--green-deep); }
  .ink-green-mid { fill: var(--green-mid); }
  .ink-green-pale { fill: var(--green-pale); }
  .ink-plum { fill: var(--plum-deep); }
  .ink-pink { fill: var(--pink-pale); }
  .ink-pink-mid { fill: var(--pink-mid); }
  .icon-line { fill: none; stroke-width: 5; stroke-linejoin: round; stroke-linecap: round; }
</style>
</head>
<body>
<main class="board">

  <!-- Row 1 -->
  <svg class="post post-new-you" style="left:25.6px;top:26px" viewBox="0 0 467 584">
    <defs>
      <linearGradient id="studio-white" x1="0" y1="0" x2="0" y2="1">
        <stop offset="0" stop-color="#ffffff"/><stop offset="0.7" stop-color="#f3f3f3"/><stop offset="1" stop-color="#e4e4e4"/>
      </linearGradient>
    </defs>
    <rect width="467" height="584" fill="url(#studio-white)"/>
    <circle cx="233" cy="219" r="163" fill="var(--blue-soft)"/>
    <text class="ink-blue" x="97" y="149" font-size="100" textLength="273" lengthAdjust="spacingAndGlyphs">25% OFF</text>
    <text class="ink-blue" x="97" y="206" font-size="67" textLength="273" lengthAdjust="spacingAndGlyphs">HOLIDAY SALE:</text>
    <text class="ink-blue" x="95" y="294" font-size="111" textLength="278" lengthAdjust="spacingAndGlyphs">NEW YOU</text>
    <text class="ink-blue" x="95" y="364" font-size="74" textLength="275" lengthAdjust="spacingAndGlyphs">STARTS NOW!</text>
    <g role="img" aria-label="Photo of four supplement bottles in a row">
      <rect x="70" y="422" width="337" height="142" rx="10" fill="#e9e6ea"/>
    </g>
  </svg>

  <svg class="post post-holiday-sale" style="left:258.5px;top:26px" viewBox="0 0 467 584">
    <rect width="467" height="584" fill="var(--green-deep)"/>
    <text class="ink-green-pale" x="88" y="156" font-size="110" textLength="292" lengthAdjust="spacingAndGlyphs">HOLIDAY</text>
    <text class="ink-green-mid" x="81" y="302" font-size="171" textLength="304" lengthAdjust="spacingAndGlyphs">SALE:</text>
    <text class="ink-green-pale" x="85" y="409" font-size="110" textLength="298" lengthAdjust="spacingAndGlyphs">25% OFF</text>
    <text class="ink-green-mid" x="73" y="489" font-size="86" textLength="322" lengthAdjust="spacingAndGlyphs">EVERYTHING</text>
  </svg>

  <svg class="post post-christmas" style="left:491.5px;top:26px" viewBox="0 0 467 584">
    <rect width="467" height="584" fill="var(--orchid)"/>
    <circle cx="235" cy="129" r="180" fill="var(--orchid-light)"/>
    <path d="M0 584 L0 430 Q170 600 467 530 L467 584 Z" fill="var(--plum-deep)"/>
    <g role="img" aria-label="Photo of a smiling woman presenting supplement bottles on a marble table">
      <rect x="245" y="174" width="222" height="400" rx="14" fill="#3a2a3c" opacity="0.85"/>
    </g>
    <text class="ink-plum" x="55" y="129" font-size="129" textLength="352" lengthAdjust="spacingAndGlyphs">25% OFF</text>
    <text class="ink-plum" x="53" y="186" font-size="60" textLength="280" lengthAdjust="spacingAndGlyphs">CHRISTMAS SALE</text>
    <g class="icon-gift icon-line" stroke="var(--plum-deep)">
      <rect x="357" y="158" width="36" height="30"/>
      <rect x="353" y="148" width="44" height="11"/>
      <line x1="375" y1="148" x2="375" y2="188"/>
      <path d="M375 148 C365 134 352 140 362 148 M375 148 C385 134 398 140 388 148"/>
    </g>
    <circle cx="123" cy="349" r="122" fill="var(--plum-deep)"/>
    <text class="ink-pink" x="70" y="311" font-size="77" textLength="107" lengthAdjust="spacingAndGlyphs">FEEL</text>
    <text class="ink-pink" x="20" y="371" font-size="79" textLength="205" lengthAdjust="spacingAndGlyphs">AMAZING</text>
    <text class="ink-pink" x="55" y="434" font-size="83" textLength="148" lengthAdjust="spacingAndGlyphs">AGAIN!</text>
  </svg>

  <svg class="post post-holiday-treat" style="left:724px;top:26px" viewBox="0 0 467 584">
    <defs>
      <linearGradient id="dark-studio" x1="0" y1="0" x2="0" y2="1">
        <stop offset="0" stop-color="#2b2b2b"/><stop offset="0.6" stop-color="#3d3d3d"/><stop offset="1" stop-color="#1c1c1c"/>
      </linearGradient>
    </defs>
    <g role="img" aria-label="Photo of supplement bottles on white stone against a dark backdrop">
      <rect width="467" height="584" fill="url(#dark-studio)"/>
    </g>
    <circle cx="234" cy="184" r="162" fill="var(--blue-deep)"/>
    <text class="ink-blue-pale" x="88" y="149" font-size="71" textLength="293" lengthAdjust="spacingAndGlyphs">HOLIDAY TREAT:</text>
    <text class="ink-blue-pale" x="88" y="234" font-size="111" textLength="293" lengthAdjust="spacingAndGlyphs">25% OFF</text>
    <text class="ink-blue-pale" x="91" y="286" font-size="63" textLength="287" lengthAdjust="spacingAndGlyphs">YOUR FAVORITES</text>
  </svg>

  <svg class="post post-reset" style="left:957px;top:26px" viewBox="0 0 467 584">
    <rect width="467" height="584" fill="var(--mint-bg)"/>
    <circle cx="234" cy="134" r="205" fill="var(--mint-circle)"/>
    <path d="M0 584 L0 545 Q250 600 467 470 L467 584 Z" fill="var(--green-deep)"/>
    <g role="img" aria-label="Photo of a smiling woman behind a row of supplement bottles">
      <rect x="40" y="174" width="260" height="380" rx="14" fill="#e9ece9" opacity="0.9"/>
    </g>
    <text class="ink-green-deep" x="54" y="129" font-size="129" textLength="337" lengthAdjust="spacingAndGlyphs">25% OFF</text>
    <text class="ink-green-deep" x="54" y="186" font-size="60" textLength="282" lengthAdjust="spacingAndGlyphs">ALL SUPPLEMENTS</text>
    <path class="icon-sparkle icon-line" stroke="var(--green-deep)" d="M368 142 Q371 162 388 165 Q371 168 368 188 Q365 168 348 165 Q365 162 368 142 Z M388 140 Q389 148 396 149 Q389 150 388 158 Q387 150 380 149 Q387 148 388 140 Z"/>
    <circle cx="371" cy="324" r="100" fill="var(--green-deep)"/>
    <text class="ink-green-pale" x="291" y="324" font-size="57" textLength="165" lengthAdjust="spacingAndGlyphs">NEW YEAR</text>
    <text class="ink-green-pale" x="318" y="374" font-size="57" textLength="110" lengthAdjust="spacingAndGlyphs">RESET!</text>
  </svg>

  <!-- Row 2 -->
  <svg class="post post-magic" style="left:25.6px;top:313.5px" viewBox="0 0 467 584">
    <rect width="467" height="584" fill="url(#studio-white)"/>
    <circle cx="233" cy="217" r="155" fill="var(--blue-soft)"/>
    <text class="ink-blue" x="97" y="117" font-size="60" textLength="273" lengthAdjust="spacingAndGlyphs">HOLIDAY MAGIC:</text>
    <text class="ink-blue" x="103" y="197" font-size="97" textLength="260" lengthAdjust="spacingAndGlyphs">25% OFF</text>
    <text class="ink-blue" x="105" y="305" font-size="133" textLength="258" lengthAdjust="spacingAndGlyphs">EVERY</text>
    <text class="ink-blue" x="103" y="367" font-size="71" textLength="260" lengthAdjust="spacingAndGlyphs">SUPPLEMENT</text>
    <g role="img" aria-label="Photo of four supplement bottles in a row">
      <rect x="70" y="420" width="337" height="142" rx="10" fill="#e9e6ea"/>
    </g>
  </svg>

  <svg class="post post-new-year-you" style="left:258.5px;top:313.5px" viewBox="0 0 467 584">
    <rect width="467" height="584" fill="var(--plum)"/>
    <text class="ink-pink" x="72" y="187" font-size="114" textLength="323" lengthAdjust="spacingAndGlyphs">25% OFF</text>
    <text class="ink-pink-mid" x="72" y="267" font-size="79" textLength="323" lengthAdjust="spacingAndGlyphs">EVERYTHING:</text>
    <text class="ink-pink" x="73" y="357" font-size="103" textLength="319" lengthAdjust="spacingAndGlyphs">NEW YEAR</text>
    <text class="ink-pink-mid" x="73" y="457" font-size="117" textLength="319" lengthAdjust="spacingAndGlyphs">NEW YOU</text>
  </svg>

  <svg class="post post-kickstart" style="left:491.5px;top:313.5px" viewBox="0 0 467 584">
    <g role="img" aria-label="Photo of supplement bottles on white stone against a dark backdrop">
      <rect width="467" height="584" fill="url(#dark-studio)"/>
    </g>
    <circle cx="233" cy="182" r="165" fill="var(--blue-deep)"/>
    <text class="ink-blue-pale" x="95" y="169" font-size="100" textLength="275" lengthAdjust="spacingAndGlyphs">25% OFF</text>
    <text class="ink-blue-pale" x="90" y="217" font-size="53" textLength="287" lengthAdjust="spacingAndGlyphs">TO KICKSTART YOUR</text>
    <text class="ink-blue-pale" x="150" y="262" font-size="57" textLength="167" lengthAdjust="spacingAndGlyphs">NEW YEAR</text>
    <text class="ink-blue-pale" x="183" y="307" font-size="57" textLength="102" lengthAdjust="spacingAndGlyphs">GOALS</text>
  </svg>

  <svg class="post post-waistline" style="left:724px;top:313.5px" viewBox="0 0 467 584">
    <rect width="467" height="584" fill="var(--mint-bg)"/>
    <circle cx="234" cy="137" r="205" fill="var(--mint-circle)"/>
    <path d="M0 584 L0 545 Q250 600 467 470 L467 584 Z" fill="var(--green-deep)"/>
    <g role="img" aria-label="Photo of a smiling woman behind a row of supplement bottles">
      <rect x="46" y="187" width="250" height="370" rx="14" fill="#e9ece9" opacity="0.9"/>
    </g>
    <text class="ink-green-deep" x="58" y="137" font-size="107" textLength="353" lengthAdjust="spacingAndGlyphs">NEW YEAR,</text>
    <text class="ink-green-deep" x="58" y="205" font-size="76" textLength="356" lengthAdjust="spacingAndGlyphs">NEW  WAISTLINE!</text>
    <circle cx="378" cy="347" r="100" fill="var(--green-deep)"/>
    <text class="ink-green-pale" x="311" y="352" font-size="57" textLength="137" lengthAdjust="spacingAndGlyphs">25% OFF</text>
    <text class="ink-green-pale" x="334" y="402" font-size="64" textLength="87" lengthAdjust="spacingAndGlyphs">SALE</text>
  </svg>

  <svg class="post post-better-you" style="left:957px;top:313.5px" viewBox="0 0 467 584">
    <rect width="467" height="584" fill="var(--orchid)"/>
    <circle cx="236" cy="127" r="200" fill="var(--orchid-light)"/>
    <path d="M0 584 L0 440 Q180 600 467 530 L467 584 Z" fill="var(--plum-deep)"/>
    <g role="img" aria-label="Photo of a smiling woman presenting supplement bottles on a marble table">
      <rect x="226" y="172" width="230" height="385" rx="14" fill="#3a2a3c" opacity="0.85"/>
    </g>
    <text class="ink-plum" x="44" y="105" font-size="94" textLength="380" lengthAdjust="spacingAndGlyphs">A BETTER YOU</text>
    <text class="ink-plum" x="44" y="185" font-size="97" textLength="380" lengthAdjust="spacingAndGlyphs">BEGINS WITH</text>
    <circle cx="121" cy="307" r="88" fill="var(--plum-deep)"/>
    <text class="ink-pink" x="74" y="312" font-size="81" textLength="100" lengthAdjust="spacingAndGlyphs">25%</text>
    <text class="ink-pink" x="84" y="372" font-size="79" textLength="80" lengthAdjust="spacingAndGlyphs">OFF</text>
  </svg>

</main>
</body>
</html>
```